Harbor Crest Residential Business Card Design - Logo Provided

business card design - LOGO PROVIDED. private capital fund investing in: commercial real estate (apartments), asset backed lending, private credit, flexible capital

Target Market(s)

private capital: commercial real estate (apartments), asset backed lending, private credit, flexible capital

Industry/Entity Type

alternative asset management

Contact Information for Business Card

logo, name, title, phone number, email and website

Font styles to use
Sans Serif

Colors
0054AA
0677BA
7BADD7
CADEEF
E8F1F8
EB3D1F
EC4F4E
F09395
F8D3D4
FCEDEE

Requirements
Must have
• use of logo on both sides and a qr code on the back

```html
<!DOCTYPE html>
<html lang="en">
<head>
<meta charset="utf-8">
<title>Harbor Crest Residential — Business Card</title>
<link href="https://fonts.googleapis.com/css2?family=Lato:wght@400;700;900&display=swap" rel="stylesheet">
<style>
  :root {
    --backdrop: #161616;
    --card: #e8e8e8;
    --red: #eb3d1f;
    --red-light: #ec4f4e;
    --blue: #0054aa;
    --blue-mid: #0677ba;
    --blue-soft: #7badd7;
    --ink: #1d1d1d;
    --faint: rgba(0, 84, 170, 0.07);
  }
  * { margin: 0; padding: 0; box-sizing: border-box; }
  html, body { width: 1200px; height: 1000px; overflow: hidden; }
  body {
    background: var(--backdrop);
    font-family: "Lato", sans-serif;
    position: relative;
  }
  .card {
    position: absolute;
    left: 215px;
    width: 770px;
    border-radius: 28px;
    background: var(--card);
    overflow: hidden;
    box-shadow: 0 6px 18px rgba(0,0,0,0.5);
  }
  .card--front { top: 46px; height: 439px; border: 2px solid var(--red); }
  .card--back { top: 515px; height: 438px; border: 2px solid var(--blue); }

  .band {
    position: absolute;
    left: 70px; right: 70px; bottom: 0;
    height: 13px;
    border-radius: 14px 14px 0 0;
  }
  .band--red { background: linear-gradient(90deg, var(--red), var(--red-light), var(--red)); }
  .band--blue { background: linear-gradient(90deg, var(--blue), var(--blue-mid), var(--blue)); }

  .brand-mark {
    position: absolute;
    display: flex;
    align-items: center;
    gap: 14px;
    z-index: 1;
  }
  .brand-mark__square { width: 26px; height: 26px; background: var(--red); flex: none; }
  .brand-mark__name {
    font-weight: 900;
    color: var(--blue);
    line-height: 1.05;
    text-transform: uppercase;
  }
  .card--front .brand-mark { left: 290px; top: 110px; }
  .card--front .brand-mark__name { font-size: 36px; width: 240px; }

  .front-name {
    position: absolute;
    left: 0; right: 0; top: 320px;
    text-align: center;
    font-size: 30px;
    font-weight: 900;
    color: var(--blue);
    letter-spacing: 1px;
    text-transform: uppercase;
  }

  .person { position: absolute; left: 53px; top: 70px; z-index: 1; }
  .person__name { font-size: 35px; font-weight: 700; color: var(--red); line-height: 1.05; }
  .person__title { font-size: 17px; color: var(--ink); margin-top: 4px; }

  .contacts { position: absolute; left: 56px; top: 170px; list-style: none; z-index: 1; }
  .contacts li {
    display: flex; align-items: center; gap: 8px;
    font-size: 21px; color: var(--ink); height: 37px;
  }
  .contacts svg { width: 18px; height: 18px; fill: var(--blue); }

  .divider {
    position: absolute; left: 374px; top: 55px;
    width: 40px; height: 260px;
    background: radial-gradient(ellipse at left center, rgba(0,0,0,0.18), rgba(0,0,0,0) 70%);
  }

  .card--back .brand-mark { left: 490px; top: 150px; }
  .card--back .brand-mark__name { font-size: 26px; width: 180px; }

  .ghost-name {
    position: absolute; left: 4px; top: 288px;
    font-size: 44px; font-weight: 900; line-height: 1.05;
    color: var(--faint); text-transform: uppercase; width: 220px;
    z-index: 0;
  }

  .address {
    position: absolute; left: 91px; top: 361px;
    font-size: 16px; color: var(--ink);
    z-index: 1;
  }
</style>
</head>
<body>
  <section class="card card--front">
    <div class="brand-mark">
      <span class="brand-mark__square"></span>
      <span class="brand-mark__name">Harbor Crest Residential</span>
    </div>
    <p class="front-name">Harbor Crest Residential</p>
    <div class="band band--red"></div>
  </section>

  <section class="card card--back">
    <div class="ghost-name" aria-hidden="true">Harbor Crest</div>
    <div class="person">
      <h1 class="person__name">CLARA VOSS</h1>
      <p class="person__title">Managing Director</p>
    </div>
    <ul class="contacts">
      <li>
        <svg viewBox="0 0 24 24"><path d="M6.6 10.8a15.1 15.1 0 0 0 6.6 6.6l2.2-2.2a1 1 0 0 1 1-.25 11.4 11.4 0 0 0 3.6.57 1 1 0 0 1 1 1V20a1 1 0 0 1-1 1A17 17 0 0 1 3 4a1 1 0 0 1 1-1h3.5a1 1 0 0 1 1 1c0 1.25.2 2.45.57 3.6a1 1 0 0 1-.25 1z"/></svg>
        044-555 210 734
      </li>
      <li>
        <svg viewBox="0 0 24 24"><path d="M2 5h20v14H2z"/><path d="M3 6l9 6.3L21 6" fill="none" stroke="#e8e8e8" stroke-width="1.6"/></svg>
        hello@harborcrest.com
      </li>
      <li>
        <svg viewBox="0 0 24 24"><circle cx="12" cy="12" r="9.5" fill="none" stroke="var(--blue)" stroke-width="2"/><path d="M2.5 12h19M12 2.5c3 3 3 16 0 19M12 2.5c-3 3-3 16 0 19" fill="none" stroke="var(--blue)" stroke-width="1.6"/></svg>
        www.harborcrest.com
      </li>
    </ul>
    <div class="divider"></div>
    <div class="brand-mark">
      <span class="brand-mark__square"></span>
      <span class="brand-mark__name">Harbor Crest Residential</span>
    </div>
    <p class="address">412 Cedar Row Linwood, FL 33120, 7745 Gulfview Parkway Bayside, FL 33941</p>
    <div class="band band--blue"></div>
  </section>
</body>
</html>
```